Surviving Domestic Violence Flyer

I need a flyer that "POPS" to attract participants for my research project. I have added the important information on my draft flyer.

```html
<!DOCTYPE html>
<html lang="en">
<head>
<meta charset="utf-8">
<title>Request for Study Participants</title>
<link href="https://fonts.googleapis.com/css2?family=Bebas+Neue&family=Raleway:wght@300;400;600&display=swap" rel="stylesheet">
<style>
  :root {
    --stage: #231f20;
    --magenta: #ec008c;
    --magenta-soft: #f49ac9;
    --yellow: #ffdd15;
    --white: #ffffff;
  }
  * { margin: 0; padding: 0; box-sizing: border-box; }
  html, body { width: 1200px; height: 900px; overflow: hidden; background: var(--stage); }
  .flyer {
    position: absolute; left: 307px; top: 25px; width: 598px; height: 873px;
    background: var(--magenta); overflow: hidden;
    font-family: "Raleway", Arial, sans-serif; text-align: center;
  }
  .hero-art {
    position: absolute; left: 0; top: 0; width: 598px; height: 300px;
    background:
      radial-gradient(ellipse at 12% 20%, rgba(255,255,255,0.85) 0 12%, transparent 30%),
      linear-gradient(120deg, var(--yellow) 0%, var(--magenta-soft) 35%, var(--magenta) 65%, var(--magenta) 88%, var(--yellow) 100%);
  }
  .hero-art::after {
    content: ""; position: absolute; left: 0; right: 0; bottom: 0; height: 60px;
    background: linear-gradient(to bottom, transparent, var(--magenta));
  }
  .title {
    position: absolute; top: 287px; left: 0; width: 100%;
    font-family: "Bebas Neue", Impact, sans-serif; font-size: 45px; line-height: 1;
    color: var(--white); letter-spacing: 0.5px;
  }
  .subtitle {
    position: absolute; top: 338px; left: 0; width: 100%;
    font-family: "Bebas Neue", Impact, sans-serif; font-size: 18px; line-height: 1;
    color: var(--yellow); letter-spacing: 0.6px;
  }
  .criteria {
    position: absolute; left: 34px; top: 362px; width: 516px; height: 177px;
    background: var(--yellow); border-radius: 12px;
    list-style: none; padding-top: 12px;
    color: var(--magenta); font-size: 14.5px; font-weight: 400; line-height: 25.5px;
  }
  .criteria li::before { content: "\2022\00a0"; }
  .criteria li.no-bullet::before { content: ""; }
  .note {
    position: absolute; left: 40px; width: 518px;
    color: var(--yellow); font-size: 9px; font-weight: 300; line-height: 12px;
  }
  .eligibility { top: 558px; }
  .contact { top: 593px; }
  .compensation { top: 621px; font-size: 11px; font-weight: 600; }
  .investigator { top: 648px; }
  .tear-offs {
    position: absolute; left: 0; top: 708px; width: 598px; height: 165px;
    background: var(--yellow); display: flex;
  }
  .tab {
    flex: 1; border-right: 1px dashed var(--magenta);
    writing-mode: vertical-rl; transform: rotate(180deg);
    display: flex; flex-direction: row; justify-content: flex-start; align-items: center;
    padding-bottom: 6px;
    color: var(--magenta); font-size: 10.5px; font-weight: 300; line-height: 13px;
  }
  .tab:first-child { border-left: none; }
</style>
</head>
<body>
<main class="flyer">
  <div class="hero-art" role="img" aria-label="Illustration of a woman's profile silhouette with flowers and swirling hair"></div>

  <h1 class="title">Request for Study Participants</h1>
  <h2 class="subtitle">Efficency of Resources Available to Survivors of Intemate Partner Abuse</h2>

  <ul class="criteria">
    <li>Are you eighteen years or older?</li>
    <li>Have you been a victim of domestic violence?</li>
    <li>Have you sought assistance with the abuse in the last 12 months?</li>
    <li>Are you still in contact with the person that abused you?</li>
    <li>Are you willing and open to discussing your experience with abuse and</li>
    <li class="no-bullet">your attempts to access services or resources?</li>
  </ul>

  <p class="note eligibility">If you answered yes to all of these questions, you may be eligable to participate in a study to better understand the resources needed and services expected for survivors of domestic violence.</p>
  <p class="note contact">Please contact Dana Whitfield at 1(555)014-2290 or via email survivorstudy@example.org for additional information.</p>
  <p class="note compensation">Participants will be compensated for their time.</p>
  <p class="note investigator">Principal Investigator: Dana Whitfield<br>Institutional Affiliation: Lakeshore State University, Dept. of Criminology, Law and Justice<br>Contact Address: Post Office Box 100245, Fairview, IL, 60000</p>

  <div class="tear-offs">
    <div class="tab"><span>Survivor Resources Study</span><span>1(555)014-2290</span></div>
    <div class="tab"><span>Survivor Resources Study</span><span>1(555)014-2290</span></div>
    <div class="tab"><span>Survivor Resources Study</span><span>1(555)014-2290</span></div>
    <div class="tab"><span>Survivor Resources Study</span><span>1(555)014-2290</span></div>
    <div class="tab"><span>Survivor Resources Study</span><span>1(555)014-2290</span></div>
    <div class="tab"><span>Survivor Resources Study</span><span>1(555)014-2290</span></div>
    <div class="tab"><span>Survivor Resources Study</span><span>1(555)014-2290</span></div>
    <div class="tab"><span>Survivor Resources Study</span><span>1(555)014-2290</span></div>
    <div class="tab"><span>Survivor Resources Study</span><span>1(555)014-2290</span></div>
    <div class="tab"><span>Survivor Resources Study</span><span>1(555)014-2290</span></div>
    <div class="tab"><span>Survivor Resources Study</span><span>1(555)014-2290</span></div>
    <div class="tab"><span>Survivor Resources Study</span><span>1(555)014-2290</span></div>
    <div class="tab"><span>Survivor Resources Study</span><span>1(555)014-2290</span></div>
    <div class="tab"><span>Survivor Resources Study</span><span>1(555)014-2290</span></div>
    <div class="tab"><span>Survivor Resources Study</span><span>1(555)014-2290</span></div>
    <div class="tab"><span>Survivor Resources Study</span><span>1(555)014-2290</span></div>
    <div class="tab"><span>Survivor Resources Study</span><span>1(555)014-2290</span></div>
  </div>
</main>
</body>
</html>
```